Pediatric Dental Practice needs a postcard for direct mail advertising

We are looking for a creative and professional double-sided postcard design for a direct mail marketing campaign. Our goal is to attract new families to our pediatric dental practice by conveying a sense of warmth, modern care, and clinical excellence. The design should feel "boutique" and high-end yet remain fun and approachable for parents and children.

```html
<!DOCTYPE html>
<html lang="en">
<head>
<meta charset="utf-8">
<title>Maple Grove Pediatric Dentistry – Direct Mail Postcard</title>
<link href="https://fonts.googleapis.com/css2?family=Montserrat:wght@400;500;600;700;800&family=Great+Vibes&display=swap" rel="stylesheet">
<style>
  :root{
    --green:#1f9a4f;
    --green-dark:#16823f;
    --green-light:#5cbf7a;
    --green-pale:#b9e2c3;
    --green-mist:#e3f3e7;
    --ink:#2a2f2c;
    --paper:#ffffff;
    --backdrop:#e9ecea;
  }
  *{box-sizing:border-box;margin:0;padding:0}
  html,body{width:1117px;height:1200px;overflow:hidden}
  body{background:var(--backdrop);font-family:"Montserrat",sans-serif;color:var(--ink);position:relative}
  .card{position:absolute;left:148px;width:820px;height:546px;background:var(--paper);overflow:hidden;box-shadow:0 6px 22px rgba(0,0,0,.12)}
  .card--front{top:36px}
  .card--back{top:618px}
  .abs{position:absolute}

  /* FRONT */
  .hero-art{position:absolute;left:0;top:0;width:820px;height:546px}
  .brand{left:34px;top:36px;width:230px;text-align:center}
  .brand__dot{width:54px;height:54px;border-radius:50%;background:var(--green-pale);margin:0 auto 14px}
  .brand__name{font-size:34px;font-weight:500;color:#3a3f3c;line-height:1;letter-spacing:.5px}
  .brand__sub{font-size:11.5px;font-weight:500;letter-spacing:4px;color:#3a3f3c;margin-top:8px}
  .headline{left:33px;top:212px;line-height:1}
  .headline__small{font-size:44px;font-weight:500;color:var(--green-light);display:block}
  .headline__big{font-size:68px;font-weight:800;color:var(--green);display:block;margin-top:4px;letter-spacing:-.5px}
  .tagline{left:33px;top:390px;border-left:2px solid var(--ink);padding-left:10px;font-size:21px;font-weight:500;line-height:1.1}
  .welcome{left:395px;top:362px;width:270px;height:110px}
  .welcome__now{position:absolute;left:148px;top:0;font-size:27px;font-weight:500}
  .welcome__script{position:absolute;left:0;top:2px;font-family:"Great Vibes",cursive;font-size:72px;color:var(--green);line-height:1}
  .welcome__new{position:absolute;left:20px;top:68px;font-size:27px;font-weight:500}
  .dots{display:grid;gap:7px}
  .dots span{width:4px;height:4px;border-radius:50%;background:var(--green-pale)}
  .dots--a{left:272px;top:58px;grid-template-columns:repeat(2,4px)}
  .dots--b{left:718px;top:422px;grid-template-columns:repeat(5,4px)}
  .promise-band{left:0;top:484px;width:820px;height:27px;background:var(--green);color:#fff;font-size:13.5px;font-weight:500;display:flex;align-items:center;padding-left:44px}

  /* BACK */
  .intro-art{position:absolute;left:0;top:0;width:460px;height:250px}
  .intro{left:34px;top:30px;color:#fff;width:400px}
  .intro__title{font-size:27px;line-height:1;font-weight:400}
  .intro__title b{font-weight:800;display:block}
  .intro__text{font-size:12.5px;line-height:1.28;margin-top:18px;font-weight:500}
  .why{left:35px;top:262px;font-size:24px;font-weight:500;color:var(--green-light)}
  .why b{color:var(--green);font-weight:800}
  .reasons{left:35px;top:310px;list-style:none}
  .reasons li{display:flex;align-items:center;height:32px;font-size:14.5px;font-weight:600}
  .reasons svg{width:22px;height:22px;margin-right:15px;flex:none}
  .stamp{left:656px;top:33px;width:131px;height:155px;border:1.5px solid #444}
  .address-line{left:474px;width:313px;height:1.5px;background:#6a6a6a}
  .contact-band{left:0;top:483px;width:820px;height:45px;background:linear-gradient(90deg,var(--green) 0%,var(--green) 62%,#cfe9d6 96%,#fff 100%);border-top:2px solid var(--green-pale)}
  .phone-pill{left:0;top:474px;width:334px;height:62px;background:var(--green);border-radius:0 26px 26px 0;border:3px solid var(--green-pale);border-left:0;display:flex;align-items:center;padding-left:40px;color:#fff;font-size:29px;font-weight:700}
  .phone-pill svg,.email svg{width:26px;height:26px;margin-right:14px}
  .email{left:352px;top:490px;display:flex;align-items:center;color:#fff;font-size:15.5px;font-weight:500}
  .email svg{width:20px;height:20px;margin-right:12px}
</style>
</head>
<body>

<section class="card card--front" aria-label="Postcard front">
  <svg class="hero-art" viewBox="0 0 820 546" aria-hidden="false">
    <defs>
      <linearGradient id="roomTone" x1="0" y1="0" x2="1" y2="1">
        <stop offset="0" stop-color="#eef2dc"/>
        <stop offset=".45" stop-color="#e6e2c0"/>
        <stop offset=".7" stop-color="#9fd2cc"/>
        <stop offset="1" stop-color="#d7b98a"/>
      </linearGradient>
      <linearGradient id="fadeLeft" x1="0" y1="0" x2="1" y2="0">
        <stop offset="0" stop-color="#fff" stop-opacity="1"/>
        <stop offset=".25" stop-color="#fff" stop-opacity="0"/>
      </linearGradient>
    </defs>
    <path d="M820,0 V330 C790,395 700,420 600,405 C520,392 470,372 420,372 V0 Z" fill="var(--green-mist)"/>
    <path d="M820,0 V300 C790,370 700,395 610,385 C530,376 470,355 400,360 V0 Z" fill="var(--green-pale)"/>
    <path d="M808,0 C822,120 800,270 700,340 C630,388 540,372 470,352 C430,340 395,342 372,352 V0 Z" fill="var(--green-light)"/>
    <g role="img" aria-label="Photo of a bright children's dental treatment room with a teal chair by a window">
      <path d="M792,0 C806,120 786,258 690,324 C622,370 536,356 468,336 C428,324 392,330 345,345 V0 Z" fill="url(#roomTone)"/>
      <path d="M792,0 C806,120 786,258 690,324 C622,370 536,356 468,336 C428,324 392,330 345,345 V0 Z" fill="url(#fadeLeft)"/>
    </g>
  </svg>

  <div class="abs brand">
    <div class="brand__dot"></div>
    <div class="brand__name">maple grove</div>
    <div class="brand__sub">PEDIATRIC DENTISTRY</div>
  </div>
  <div class="abs dots dots--a"><span></span><span></span><span></span><span></span><span></span><span></span></div>

  <h1 class="abs headline">
    <span class="headline__small">Little Smiles.</span>
    <span class="headline__big">Big Care.</span>
  </h1>

  <p class="abs tagline">Gentle, modern dentistry<br>designed just for children.</p>

  <div class="abs welcome">
    <span class="welcome__now">Now</span>
    <span class="welcome__script">Welcoming</span>
    <span class="welcome__new">New Patients</span>
  </div>
  <div class="abs dots dots--b"><span></span><span></span><span></span><span></span><span></span><span></span><span></span><span></span><span></span><span></span><span></span><span></span><span></span><span></span><span></span></div>

  <div class="abs promise-band">Creating confident smiles in a calm, friendly environment — where kids feel safe and parents feel reassured.</div>
</section>

<section class="card card--back" aria-label="Postcard back">
  <svg class="intro-art" viewBox="0 0 460 250">
    <defs>
      <linearGradient id="clinicTone" x1="0" y1="0" x2="1" y2="1">
        <stop offset="0" stop-color="#2a9c55"/>
        <stop offset=".6" stop-color="#1f8a47"/>
        <stop offset="1" stop-color="#3aa963"/>
      </linearGradient>
    </defs>
    <path d="M0,0 H448 V170 C448,215 425,238 370,240 H0 Z" fill="var(--green-pale)"/>
    <path d="M0,0 H436 V160 C436,205 414,228 360,230 H0 Z" role="img" aria-label="Green-toned photo of the practice reception area" fill="url(#clinicTone)"/>
  </svg>

  <div class="abs intro">
    <h2 class="intro__title">A Better<b>Dental Experience</b>for Your Child</h2>
    <p class="intro__text">At Maple Grove Pediatric Dentistry, we believe every child deserves a positive start to their dental journey.<br>Our boutique-style practice combines advanced technology with a warm, personalised approach — helping children feel relaxed, comfortable, and cared for at every visit.</p>
  </div>

  <h3 class="abs why">Why Parents <b>Choose Us:</b></h3>
  <ul class="abs reasons">
    <li><svg viewBox="0 0 24 24" fill="none" stroke="var(--green)" stroke-width="1.6"><path d="M12 20s-7-4.5-7-10a4 4 0 0 1 7-2.5A4 4 0 0 1 19 10c0 5.5-7 10-7 10z"/></svg>Gentle, child-focused care</li>
    <li><svg viewBox="0 0 24 24" fill="none" stroke="var(--green)" stroke-width="1.6"><path d="M4 14h12l3-4M6 14v5M14 14v5M4 19h12M7 10V5M5 5h4"/></svg>Calm, modern, boutique environment</li>
    <li><svg viewBox="0 0 24 24" fill="none" stroke="var(--green)" stroke-width="1.6"><circle cx="7" cy="7" r="2.5"/><circle cx="17" cy="7" r="2.5"/><circle cx="12" cy="14" r="2.5"/><path d="M3 21v-2a4 4 0 0 1 4-4M21 21v-2a4 4 0 0 0-4-4"/></svg>Friendly and experienced team</li>
    <li><svg viewBox="0 0 24 24" fill="none" stroke="var(--green)" stroke-width="1.6"><path d="M7 3c-3 0-4 3-3 6 1 3 1 7 2 10 .5 1.5 2 1.5 2.5 0L10 14h4l1.5 5c.5 1.5 2 1.5 2.5 0 1-3 1-7 2-10 1-3 0-6-3-6-2 0-3 1-5 1S9 3 7 3z"/></svg>Preventive &amp; comprehensive pediatric dentistry</li>
    <li><svg viewBox="0 0 24 24" fill="none" stroke="var(--green)" stroke-width="1.6"><circle cx="12" cy="12" r="9"/><path d="M8 13.5c1 2 7 2 8 0"/><circle cx="9" cy="9.5" r=".8" fill="var(--green)"/><circle cx="15" cy="9.5" r=".8" fill="var(--green)"/></svg>Designed to make kids feel safe and confident</li>
  </ul>

  <div class="abs stamp"></div>
  <div class="abs address-line" style="top:260px"></div>
  <div class="abs address-line" style="top:315px"></div>
  <div class="abs address-line" style="top:372px"></div>
  <div class="abs address-line" style="top:426px"></div>

  <div class="abs contact-band"></div>
  <div class="abs phone-pill">
    <svg viewBox="0 0 24 24" fill="none" stroke="#fff" stroke-width="2"><path d="M5 3h4l2 5-2.5 1.5a11 11 0 0 0 6 6L16 13l5 2v4a2 2 0 0 1-2 2A17 17 0 0 1 3 5a2 2 0 0 1 2-2z"/></svg>(555) 014-2780
  </div>
  <div class="abs email">
    <svg viewBox="0 0 24 24" fill="none" stroke="#fff" stroke-width="1.8"><circle cx="12" cy="12" r="9"/><path d="M3 12h18M12 3c3 3 3 15 0 18M12 3c-3 3-3 15 0 18"/></svg>hello@maplegrovekids.com
  </div>
</section>

</body>
</html>
```